Refresh www.pollbrightclass.com.au & design new logo

We need a new refreshed website for our site www.pollbrightclass.com.au

We provide an survey service for schools, providing feedback from teachers, students and parents. The survey functionality is done through query otter, so the refresh is simply for the website, which needs to sell the service to our target market which is mainly principals of school.

We want a new fresh look, so are looking for a logo redesign as well. We are flexible with colours as well (does not need to be the same blue as is used at the moment.

Re the website, We are happy to look at Navigation and page changes. Also need to include a call to action- perhaps a "sign up now" or email for more information on the home page. I have used a wordpress site before, but an not an expert. Items I would like to edit in the future is pricing, changing the sample reports to be sent out etc.

Target Market(s)

Principals and teachers of schools who are seeking formative feedback from their parents, students and teachers

Industry/Entity Type

School

Font styles to use
Serif
Sans Serif

Colors

Designer to choose colors to be used in the design.

Requirements
Must have
• Call to action on home page- inviting to email for more information
Link to video explaining the surveys
Ability to download sample reports
home/sample reports/parents/teachers/parents/testimonials/about us/benefits/pricing

```html
<!DOCTYPE html>
<html lang="en">
<head>
<meta charset="utf-8">
<title>Poll Bright Class</title>
<link href="https://fonts.googleapis.com/css2?family=Arimo:wght@400;700&family=Lato:wght@400&display=swap" rel="stylesheet">
<style>
:root{
  --header-blue:#4169b8;
  --nav-blue:#24427a;
  --nav-active:#0f1e3d;
  --label-blue:#243f73;
  --green:#33c41a;
  --green-dark:#238a12;
  --panel:#e2e4ea;
  --video-panel:#d6d6d6;
  --text:#5a5f6e;
  --heading:#2a4a8a;
  --white:#ffffff;
}
*{margin:0;padding:0;box-sizing:border-box}
html,body{width:1200px;height:1152px;overflow:hidden;background:var(--white)}
body{position:relative;font-family:"Arimo",Arial,sans-serif;color:var(--text)}
.site-header{position:absolute;left:0;top:0;width:1200px;height:170px;background:var(--header-blue)}
.brand{position:absolute;left:62px;top:34px;display:flex;align-items:center;gap:14px}
.brand-dot{width:46px;height:46px;border-radius:50%;background:var(--white)}
.brand-name{color:var(--white);font-weight:700;font-size:36px;line-height:33px;letter-spacing:-.5px}
.demo-button{position:absolute;left:941px;top:49px;width:195px;height:71px;border-radius:9px;background:var(--green);box-shadow:0 4px 0 var(--green-dark);color:var(--white);font-weight:700;font-size:18px;line-height:18px;padding:16px 0 0 20px;text-decoration:none}
.demo-button svg{position:absolute;right:16px;top:11px}
.main-nav{position:absolute;left:0;top:170px;width:1200px;height:56px;background:var(--nav-blue)}
.main-nav a{position:absolute;top:0;height:56px;line-height:56px;color:var(--white);font-weight:700;font-size:16px;text-decoration:none}
.main-nav a.is-active{background:var(--nav-active);padding:0 22px;left:62px}
.survey-card{position:absolute;top:266px;height:233px}
.card-photo{position:absolute;left:0;top:0;width:324px;height:233px}
.card-label{position:absolute;top:153px;height:47px;display:flex}
.card-label span{background:var(--label-blue);color:var(--white);font-weight:700;font-size:18px;line-height:47px;text-align:center}
.card-label i{width:48px;background:var(--green);display:flex;align-items:center;justify-content:center}
.intro-panel{position:absolute;left:62px;top:542px;width:616px;height:270px;background:var(--panel);padding:22px 24px;font-size:16px;line-height:23px;color:#5b6170}
.intro-panel p+p{margin-top:18px}
.video-panel{position:absolute;left:708px;top:542px;width:430px;height:270px;background:var(--video-panel);text-align:center;padding-top:106px}
.video-panel p{font-family:"Lato",sans-serif;font-size:11px;color:#7b7b7b;margin-top:8px}
.site-footer{position:absolute;left:0;top:856px;width:1200px;height:296px;background:var(--panel)}
.footer-col{position:absolute;top:34px;width:310px;font-size:13.5px;line-height:21px;color:#6a6f7c}
.footer-col h3{font-size:18px;color:var(--heading);margin-bottom:10px}
.footer-col p+p{margin-top:12px}
.footer-rule{position:absolute;left:84px;top:192px;width:1036px;height:1px;background:#cfd2da}
.footer-note{position:absolute;left:0;top:220px;width:1200px;text-align:center;font-size:13px;color:#7a7f8c}
</style>
</head>
<body>
<header class="site-header">
  <div class="brand">
    <div class="brand-dot"></div>
    <div class="brand-name">Poll<br>Bright<br>Class</div>
  </div>
  <a class="demo-button" href="#">Try a free<br>demo now!
    <svg width="46" height="46" viewBox="0 0 46 46" fill="none" stroke="#fff" stroke-width="3" stroke-linecap="round">
      <circle cx="23" cy="23" r="10"/>
      <path d="M23 3v6M23 37v6M3 23h6M37 23h6M9 9l4 4M33 33l4 4M37 9l-4 4M13 33l-4 4"/>
    </svg>
  </a>
</header>

<nav class="main-nav">
  <a class="is-active" href="#">Home</a>
  <a href="#" style="left:160px">Sample Reports</a>
  <a href="#" style="left:314px">Parents</a>
  <a href="#" style="left:407px">Teachers</a>
  <a href="#" style="left:510px">Testimonials</a>
  <a href="#" style="left:641px">About Us</a>
  <a href="#" style="left:749px">Benefits</a>
  <a href="#" style="left:850px">Pricing</a>
</nav>

<section class="survey-card" style="left:62px">
  <div class="card-photo" role="img" aria-label="Photo of students walking to school" style="background:linear-gradient(160deg,#b39a86,#8a9a6a 55%,#c9c9c4)"></div>
  <a class="card-label" href="#" style="left:105px"><span style="width:187px">Student Surveys</span><i><svg width="14" height="16" viewBox="0 0 14 16"><path d="M3 2l7 6-7 6" fill="none" stroke="#fff" stroke-width="3"/></svg></i></a>
</section>
<section class="survey-card" style="left:431px">
  <div class="card-photo" role="img" aria-label="Photo of a family looking at a globe" style="width:318px;background:linear-gradient(150deg,#d8d3cc,#b8946f 50%,#5a7fa3)"></div>
  <a class="card-label" href="#" style="left:107px"><span style="width:187px">Parent Surveys</span><i><svg width="14" height="16" viewBox="0 0 14 16"><path d="M3 2l7 6-7 6" fill="none" stroke="#fff" stroke-width="3"/></svg></i></a>
</section>
<section class="survey-card" style="left:799px">
  <div class="card-photo" role="img" aria-label="Photo of smiling school staff" style="width:319px;background:linear-gradient(150deg,#f1ece6,#c99a7e 45%,#8c2f3e)"></div>
  <a class="card-label" href="#" style="left:129px"><span style="width:163px">Staff Surveys</span><i><svg width="14" height="16" viewBox="0 0 14 16"><path d="M3 2l7 6-7 6" fill="none" stroke="#fff" stroke-width="3"/></svg></i></a>
</section>

<section class="intro-panel">
  <p>Lorem ipsum dolor sit amet, consectetur adipiscing elit. Nulla pellentesque ex justo, quis convallis enim vestibulum in. In in venenatis nulla, id euismod massa. Nulla eu posuere risus. Etiam hendrerit tempor feugiat. Sed urna felis, sagittis vel orci non, condimentum ullamcorper tortor.</p>
  <p>Praesent auctor tellus eget lectus tempor, sit amet suscipit erat auctor. Nam porta justo ac pulvinar gravida. Nam egestas ullamcorper eleifend. Cum sociis natoque penatibus et magnis dis parturient montes, nascetur ridiculus mus. Quisque rutrum non mi non congue.</p>
</section>

<section class="video-panel">
  <svg width="38" height="30" viewBox="0 0 38 30">
    <rect width="38" height="30" fill="#8a8a8a"/>
    <g fill="#d6d6d6"><rect x="2" y="3" width="4" height="4"/><rect x="2" y="13" width="4" height="4"/><rect x="2" y="23" width="4" height="4"/><rect x="32" y="3" width="4" height="4"/><rect x="32" y="13" width="4" height="4"/><rect x="32" y="23" width="4" height="4"/><path d="M15 8l10 7-10 7z"/></g>
  </svg>
  <p>Video Coming Soon</p>
</section>

<footer class="site-footer">
  <div class="footer-col" style="left:84px">
    <h3>Contact</h3>
    <p>14 Harbour Lane<br>BAYVIEW&nbsp; QLD&nbsp; 4999</p>
    <p>Email: info@pollbrightclass.com.au</p>
    <p>Phone 0400 555 218</p>
  </div>
  <div class="footer-col" style="left:444px">
    <h3>Social</h3>
    <p>In sem arcu, gravida vitae pulvinar sit amet, iaculis a velit. Integer egestas varius neque a semper. Aliquam mollis imperdiet pretium. Integer finibus nulla sed dui ultrices sodales.</p>
  </div>
  <div class="footer-col" style="left:811px">
    <h3>Partners</h3>
    <p>In sem arcu, gravida vitae pulvinar sit amet, iaculis a velit. Integer egestas varius neque a semper. Aliquam mollis imperdiet pretium. Integer finibus nulla sed dui ultrices sodales.</p>
  </div>
  <div class="footer-rule"></div>
  <p class="footer-note">Vestibulum mollis lorem at orci sodales finibus.</p>
</footer>
</body>
</html>
```